Custom hot rod builder needs a website for launch of new business where he will build luxury garages

We need a website that gives a WOW first impression for "Vantor Hangars". This is a new business so photos are renderings but we need it to really attract a particular audience. Our initial business is custom hot rods so now we are building garages for them. These will be like luxury "homes" for cars! I will attach our new logo. Website needs to feel powerful and prestigious.

Target Market(s)

middle aged men, car enthusiasts

Industry/Entity Type

automotive, construction

Number of Pages Required

2 page

Font styles to use
Serif

Colors
0054AA
0677BA
7BADD7
CADEEF
E8F1F8

Requirements
Must have
• a WOW factor. luxury. contact form.
Nice to have
• ?

```html
<!DOCTYPE html>
<html lang="en">
<head>
<meta charset="UTF-8">
<title>Vantor Hangars — Dream Homes for Car Collectors</title>
<link rel="stylesheet" href="https://fonts.googleapis.com/css2?family=Krona+One&family=Poppins:ital,wght@0,400;0,500;0,600;1,400&display=swap">
<style>
:root{
  --blue:#0677BA;
  --blue-deep:#0054AA;
  --blue-bright:#1883cc;
  --blue-soft:#7BADD7;
  --ink:#0b0b0d;
  --slate:#1f222a;
  --panel:#2b2e35;
  --panel-line:#3a3d44;
  --form:#23262d;
  --night:#101114;
  --text:#e9ecf1;
  --muted:#b9bec7;
  --star:#f6b21a;
}
*{margin:0;padding:0;box-sizing:border-box}
html,body{width:1200px;height:3953px;overflow:hidden}
body{position:relative;background:var(--ink);color:var(--text);font-family:"Poppins",sans-serif}
.abs{position:absolute}
.display{font-family:"Krona One",sans-serif;text-transform:uppercase;letter-spacing:1px}
.btn{position:absolute;display:flex;align-items:center;justify-content:center;background:var(--blue);color:#fff;font-size:13px;font-family:"Poppins",sans-serif}
.photo{position:absolute}

/* Hero */
.hero{position:absolute;left:0;top:0;width:1200px;height:635px;background:linear-gradient(180deg,#3a2412 0%,#6b4424 30%,#4a5a50 60%,#2e3f3a 80%,#6a4a2a 100%)}
.hero-shade{position:absolute;inset:0;background:linear-gradient(180deg,rgba(0,0,0,.55) 0%,rgba(0,0,0,0) 18%,rgba(0,0,0,0) 80%,rgba(0,0,0,.25) 100%)}
.brand{position:absolute;display:flex;align-items:center;gap:10px}
.brand-dot{width:40px;height:40px;border-radius:50%;background:var(--blue-bright)}
.brand-name{font-family:"Krona One",sans-serif;color:var(--blue-bright);font-size:17px;line-height:1.1;text-transform:uppercase}
.nav a{position:absolute;top:29px;color:#fff;font-size:13px;text-decoration:none;text-transform:uppercase}
.nav .active{font-weight:600}
.nav .cta{left:744px;top:20px;width:118px;height:34px;background:var(--blue);display:flex;align-items:center;justify-content:center}
.call{position:absolute;left:885px;top:22px;display:flex;gap:8px;align-items:center;color:#fff}
.call small{display:block;font-size:13px;line-height:1.2}
.call strong{display:block;font-size:17px;font-weight:500;line-height:1.2}
.hero-title{position:absolute;left:0;width:1200px;top:307px;text-align:center;font-size:33px;line-height:40px;color:#fff;text-shadow:0 2px 8px rgba(0,0,0,.6)}

/* About */
.about{position:absolute;left:0;top:635px;width:1200px;height:523px;background:var(--ink)}
.about h2{position:absolute;left:601px;top:100px;font-size:31px;line-height:34px;color:var(--blue-bright)}
.about p{position:absolute;left:601px;width:440px;font-size:13.5px;line-height:24.5px;color:#e3e6ea}

/* Gallery */
.gallery{position:absolute;left:0;top:1158px;width:1200px;height:941px;background:var(--slate)}
.section-title{position:absolute;left:0;width:1200px;text-align:center;font-size:31px;color:var(--blue-bright)}

/* Promo */
.promo{position:absolute;left:0;top:2099px;width:1200px;height:519px;background:var(--ink)}
.promo h3{position:absolute;left:161px;top:157px;font-family:"Krona One",sans-serif;font-size:30px;line-height:46px;color:var(--blue-bright)}

/* Testimonials */
.testimonials{position:absolute;left:0;top:2618px;width:1200px;height:494px;background:var(--slate)}
.quote-box{position:absolute;left:245px;top:176px;width:708px;height:229px;background:var(--panel);border:1px solid var(--panel-line)}
.quote-mark{position:absolute;left:574px;top:150px;width:52px;height:52px;border-radius:50%;background:var(--blue-bright);display:flex;align-items:center;justify-content:center}
.quote-text{position:absolute;left:300px;width:600px;top:226px;text-align:center;font-style:italic;font-size:15px;line-height:24px;color:#e6e8ec}
.quote-name{position:absolute;left:0;width:1200px;top:350px;text-align:center;font-family:"Krona One",sans-serif;font-size:13px;color:var(--blue-bright)}
.stars{position:absolute;left:544px;top:370px;display:flex;gap:5px}
.arrow{position:absolute;top:262px;width:28px;height:58px}

/* Inquiry + footer */
.inquiry-band{position:absolute;left:0;top:3112px;width:1200px;height:451px;background:var(--night)}
.footer{position:absolute;left:0;top:3563px;width:1200px;height:390px;background:radial-gradient(ellipse at 60% 55%,#1d1f24 0%,#111216 55%,#07080a 100%)}
.form-card{position:absolute;left:245px;top:3189px;width:708px;height:425px;background:var(--form)}
.form-card h2{position:absolute;left:0;width:708px;top:76px;text-align:center;font-size:30px;color:var(--blue-bright)}
.field{position:absolute;height:24px;border-bottom:1px solid #5a5e66;display:flex;align-items:flex-start;gap:12px;font-size:13px;color:#d8dbe0;padding-left:2px}
.field svg{flex:none;margin-top:2px}
.submit{position:absolute;left:287px;top:330px;width:135px;height:39px;border-radius:20px;background:var(--blue);color:#fff;font-size:13px;display:flex;align-items:center;justify-content:center}
.footer-brand{position:absolute;left:0;width:1200px;top:3667px;display:flex;justify-content:center;align-items:center;gap:12px}
.footer-brand .brand-dot{background:#fff;width:44px;height:44px}
.footer-brand .brand-name{color:#fff;font-size:22px}
.footer-rule{position:absolute;left:161px;top:3770px;width:878px;height:1px;background:rgba(255,255,255,.12)}
.contact-item{position:absolute;top:3806px;display:flex;gap:12px;align-items:flex-start;font-size:13.5px;line-height:20px;color:#fff}
.contact-item b{font-weight:600}
.copyright{position:absolute;left:163px;top:3905px;font-size:13px;color:#fff}
.social{position:absolute;left:912px;top:3903px;display:flex;gap:18px}
.social span{width:17px;height:17px;border-radius:50%;background:#fff}
</style>
</head>
<body>

<!-- Hero -->
<header class="hero">
  <div class="photo" role="img" aria-label="Rendered interior of a luxury collector garage with brick walls, wooden ceiling, track lights and classic cars" style="inset:0;background:linear-gradient(180deg,#2b1a0c 0%,#7a4f2a 28%,#58503c 50%,#2f4a44 70%,#7a5430 100%)"></div>
  <div class="hero-shade"></div>
  <div class="brand" style="left:161px;top:22px">
    <span class="brand-dot"></span>
    <span class="brand-name">Vantor<br>Hangars</span>
  </div>
  <nav class="nav">
    <a class="active" style="left:471px">Home</a>
    <a style="left:549px">About Us</a>
    <a style="left:651px">Services</a>
    <a class="cta">Contact Us</a>
  </nav>
  <div class="call">
    <svg width="30" height="30" viewBox="0 0 24 24" fill="none" stroke="#fff" stroke-width="1.4"><path d="M5 3h3l2 5-2.5 1.5a11 11 0 0 0 6 6L15 13l5 2v3a2 2 0 0 1-2 2A16 16 0 0 1 3 5a2 2 0 0 1 2-2z"/><path d="M14 3a7 7 0 0 1 7 7M14 6.5a3.5 3.5 0 0 1 3.5 3.5"/></svg>
    <div><small>CALL US TODAY</small><strong>014 2870 316</strong></div>
  </div>
  <h1 class="hero-title display">Dream Homes for Car<br>Collectors</h1>
  <a class="btn" style="left:532px;top:402px;width:134px;height:34px">CALL US TODAY</a>
</header>

<!-- About -->
<section class="about">
  <div class="photo" role="img" aria-label="Exterior rendering of a modern garage building with glass front showing parked cars" style="left:0;top:42px;width:525px;height:389px;background:linear-gradient(180deg,#c9ccd2 0%,#b6b9bf 35%,#8a7a5a 55%,#b9bcc2 75%,#9ea1a6 100%)"></div>
  <h2 class="display">About<br>Vantor Hangars</h2>
  <p style="top:186px">Lorem ipsum dolor sit amet, consectetur adipiscing elit. Aenean sit amet sapien ante. Integer efficitur lectus eu mi elementum, non posuere libero condimentum.</p>
  <p style="top:265px">Donec ex risus, commodo id interdum et, tempor a nisl. Morbi dignissim ex in pulvinar dictum. Aenean pellentesque tortor quis purus tristique, vitae pellentesque urna sagittis. Nunc dignissim ut leo in convallis.</p>
  <a class="btn" style="left:601px;top:381px;width:135px;height:40px">Read More</a>
</section>

<!-- Gallery -->
<section class="gallery">
  <h2 class="section-title display" style="top:85px">Our Gallery</h2>
  <div class="photo" role="img" aria-label="Orange supercar in a dark showroom with geometric ceiling lights" style="left:161px;top:159px;width:368px;height:300px;background:linear-gradient(180deg,#4a4d52 0%,#1d1e21 55%,#7a2a12 75%,#2a2b2e 100%)"></div>
  <div class="photo" role="img" aria-label="Collector garage interior with wooden ceiling and classic cars" style="left:543px;top:159px;width:496px;height:300px;background:linear-gradient(180deg,#5a3a1c 0%,#8a5c30 35%,#4b5a48 65%,#2f4340 100%)"></div>
  <div class="photo" role="img" aria-label="Modern garage building exterior with palm trees and glass frontage" style="left:161px;top:473px;width:496px;height:300px;background:linear-gradient(180deg,#9aa4ae 0%,#c4c7cc 45%,#6a6d5a 65%,#a8abb0 100%)"></div>
  <div class="photo" role="img" aria-label="Silver compact car in a red-lit workshop" style="left:671px;top:473px;width:368px;height:300px;background:linear-gradient(160deg,#1b1c1f 0%,#5a1a14 45%,#8a8c90 70%,#2a1a16 100%)"></div>
  <a class="btn" style="left:532px;top:811px;width:135px;height:41px">Load More</a>
</section>

<!-- Promo -->
<section class="promo">
  <h3>Lorem Ipsum Dolor Sit<br>Amet, Consectetur<br>Adipiscing Elit.</h3>
  <a class="btn" style="left:161px;top:313px;width:135px;height:40px">Contact Us</a>
  <div class="photo" role="img" aria-label="Yellow sports car in a showroom" style="left:675px;top:91px;width:525px;height:337px;background:linear-gradient(160deg,#3a3c40 0%,#1e1f22 40%,#d8b012 60%,#8a6e08 80%,#1a1b1e 100%)"></div>
</section>

<!-- Testimonials -->
<section class="testimonials">
  <h2 class="section-title display" style="top:86px">Customer Testimonials</h2>
  <div class="quote-box"></div>
  <div class="quote-mark">
    <svg width="26" height="20" viewBox="0 0 26 20" fill="#fff"><circle cx="6" cy="12" r="6"/><path d="M1 11C1 5 5 1 10 0v3C7 4 5 7 5 11z"/><circle cx="19" cy="12" r="6"/><path d="M14 11c0-6 4-10 9-11v3c-3 1-5 4-5 8z"/></svg>
  </div>
  <p class="quote-text">Lorem ipsum dolor sit amet, consectetur adipiscing elit. Aenean sit amet sapien ante. Integer efficitur lectus eu mi elementum, non posuere libero condimentum. Donec ex risus, commodo id interdum et, tempor a nisl. Morbi dignissim ex in pulvinar dictum.</p>
  <div class="quote-name">RICK CALLOWAY</div>
  <div class="stars">
    <svg width="18" height="18" viewBox="0 0 24 24" fill="var(--star)"><path d="M12 2l3 7 7 .6-5.3 4.7 1.6 7.2L12 17.8 5.7 21.5l1.6-7.2L2 9.6 9 9z"/></svg>
    <svg width="18" height="18" viewBox="0 0 24 24" fill="var(--star)"><path d="M12 2l3 7 7 .6-5.3 4.7 1.6 7.2L12 17.8 5.7 21.5l1.6-7.2L2 9.6 9 9z"/></svg>
    <svg width="18" height="18" viewBox="0 0 24 24" fill="var(--star)"><path d="M12 2l3 7 7 .6-5.3 4.7 1.6 7.2L12 17.8 5.7 21.5l1.6-7.2L2 9.6 9 9z"/></svg>
    <svg width="18" height="18" viewBox="0 0 24 24" fill="var(--star)"><path d="M12 2l3 7 7 .6-5.3 4.7 1.6 7.2L12 17.8 5.7 21.5l1.6-7.2L2 9.6 9 9z"/></svg>
    <svg width="18" height="18" viewBox="0 0 24 24" fill="var(--star)"><path d="M12 2l3 7 7 .6-5.3 4.7 1.6 7.2L12 17.8 5.7 21.5l1.6-7.2L2 9.6 9 9z"/></svg>
  </div>
  <svg class="arrow" style="left:246px" viewBox="0 0 28 58"><path d="M0 0L28 29 0 58z" fill="#4a4d54"/><path d="M13 23l-6 6 6 6" stroke="#fff" stroke-width="2" fill="none"/></svg>
  <svg class="arrow" style="left:924px" viewBox="0 0 28 58"><path d="M28 0L0 29 28 58z" fill="var(--blue-bright)"/><path d="M15 23l6 6-6 6" stroke="#fff" stroke-width="2" fill="none"/></svg>
</section>

<!-- Inquiry + Footer -->
<div class="inquiry-band"></div>
<footer class="footer" role="img" aria-label="Dark garage with a black supercar parked in front of roller doors"></footer>

<form class="form-card">
  <h2 class="display">Quick Inquiry</h2>
  <label class="field" style="left:85px;top:168px;width:261px">
    <svg width="13" height="13" viewBox="0 0 24 24" fill="none" stroke="#d8dbe0" stroke-width="2"><circle cx="12" cy="8" r="4"/><path d="M4 22c0-5 4-8 8-8s8 3 8 8"/></svg>First Name</label>
  <label class="field" style="left:361px;top:168px;width:264px">
    <svg width="13" height="13" viewBox="0 0 24 24" fill="none" stroke="#d8dbe0" stroke-width="2"><circle cx="12" cy="8" r="4"/><path d="M4 22c0-5 4-8 8-8s8 3 8 8"/></svg>Last Name</label>
  <label class="field" style="left:85px;top:228px;width:261px">
    <svg width="13" height="13" viewBox="0 0 24 24" fill="none" stroke="#d8dbe0" stroke-width="2"><path d="M5 3h3l2 5-2.5 1.5a11 11 0 0 0 6 6L15 13l5 2v3a2 2 0 0 1-2 2A16 16 0 0 1 3 5a2 2 0 0 1 2-2z"/></svg>Phone Number</label>
  <label class="field" style="left:361px;top:228px;width:264px">
    <svg width="13" height="13" viewBox="0 0 24 24" fill="none" stroke="#d8dbe0" stroke-width="2"><rect x="2" y="5" width="20" height="14"/><path d="M2 6l10 7 10-7"/></svg>Email Address</label>
  <label class="field" style="left:85px;top:289px;width:540px">
    <svg width="13" height="13" viewBox="0 0 24 24" fill="none" stroke="#d8dbe0" stroke-width="2"><path d="M4 20l1-5L16 4l4 4L9 19z"/></svg>Your Message</label>
  <div class="submit">Submit</div>
</form>

<div class="footer-brand">
  <span class="brand-dot"></span>
  <span class="brand-name">Vantor Hangars</span>
</div>
<div class="footer-rule"></div>

<div class="contact-item" style="left:161px">
  <svg width="38" height="38" viewBox="0 0 24 24" fill="none" stroke="#fff" stroke-width="1.1"><path d="M12 21s-6-6.5-6-11a6 6 0 0 1 12 0c0 4.5-6 11-6 11z"/><circle cx="12" cy="10" r="2.2"/><ellipse cx="12" cy="21" rx="7" ry="1.6"/></svg>
  <div>48, Harbor Works, Dock Lane<br>Marlow, State QZ 604218</div>
</div>
<div class="contact-item" style="left:532px">
  <svg width="36" height="36" viewBox="0 0 24 24" fill="none" stroke="#fff" stroke-width="1.1"><path d="M5 3h3l2 5-2.5 1.5a11 11 0 0 0 6 6L15 13l5 2v3a2 2 0 0 1-2 2A16 16 0 0 1 3 5a2 2 0 0 1 2-2z"/><path d="M14 3a7 7 0 0 1 7 7M14 6.5a3.5 3.5 0 0 1 3.5 3.5"/></svg>
  <div><b>Phone</b><br>140-287-3162</div>
</div>
<div class="contact-item" style="left:829px">
  <svg width="36" height="36" viewBox="0 0 24 24" fill="none" stroke="#fff" stroke-width="1.1"><path d="M3 10l9-7 9 7v11H3z"/><path d="M3 10l9 6 9-6"/><path d="M7 8h10M7 11h10"/></svg>
  <div><b>Email</b><br>hello@vantorhangars.com</div>
</div>

<div class="copyright">© 2022 Vantor Hangars. All Rights Reserved.</div>
<div class="social" aria-label="Social links"><span></span><span></span><span></span><span></span></div>

</body>
</html>
```